CedarBight.Lawyer, a new website for Morris.

Looking for a professional web site for my small country law firm.
I have a logo, chart, map, my photo, office photo, google analytics code, my drone video on YouTube, "Brantwell Beacon Skyrun, also on www.loftcove.guide", and text content. I am figuring out how to get those into digital forms.
First page needs a professional look. Here's where I am really hoping for your skill set.
Banner should be well designed so as to "ease" the viewer into confidence in my firm
Prefer the "white backround", less cluttered style of design.
My office has been in Key Center, main and only town of Key Peninsula, for 25 years, with emphasis on real property matters. Naturally land lasts longer than people, so estates, trusts and succession issues are relevant.
Local KP is the heart of southern Puget Sound, 75 miles of spectacular residential waterfront. We have the best land, waterfront, beaches and views in Puget Sound, however of course Seattle and the San Juan Islands could not be disregarded. It's that we have the most privacy, the best old growth Doug Firs, wildlife and low population density.
Puget Sound conditions are very specific for residential development.
One must consider:
Topography, hydro-geology, geomorphology, hill slope stability, soils must support septic systems, individual wells, prescriptive, express and implied easement issues, boundary lines don't always line up with surveys or expectations, or historic use, thus adverse possession abounds environmentally protected shorelines and wetlands, all challenges, but ohh.., the views and unique, world class waterfront.
Everyone who lives on Puget Sound is convinced they live in the most beautiful and spectacular place in the world, and we're all correct.

Target Market(s)

Members of the Halvern-Ostrow County Bar Association, and more distant counsel seeking consultation re: local conditions.
Also, I decided it was time to have a website, so a reference place to direct clients.
I like the professional sound of .lawyer vs. commercial sound of .com.

Industry/Entity Type

Law Firm

Coding

Coded - Design and coding required

Number of Pages Required

5+ page

Font styles to use
Other font styles liked:
• That newly created "web" font everyone seems to be usIng

Colors
32b8a4
3377b5

Requirements
Must have
• A strong first page with my photo and Puget Sound chart professionally created.
• A page I have ready with local links.
• A "How to find me page", which should have a map, and photo of my office, which I can make with the preloaded templates the host provides.
• A "This is what I do page", with some testimonials, which I can do via said templates or preferably by professionals.
Nice to have
• Clean look.
• Consistent looks to pages.
• First comment I got back talked about just designing one page, and if requires $340.00, so be it.
• Typical local sites have 4/5 pages, so perhaps a "fill-able" generic pages, I can build myself.
• Ideally, I would step into a working site I can edit myself.
• Not looking for e-commerce site, but the remainder of language the "Smart" professional used is unknown to me.
• Bit out of my element here, hoping for guidance.
Should not have
• Clutter

```html
<!DOCTYPE html>
<html lang="en">
<head>
<meta charset="utf-8">
<title>CedarBight.Lawyer</title>
<link href="https://fonts.googleapis.com/css2?family=Marcellus&family=Roboto+Slab:wght@400&family=Open+Sans:wght@400;600&family=Roboto:wght@400&display=swap" rel="stylesheet">
<style>
:root{
  --brand:#2b3990;
  --ink:#222;
  --muted:#444;
  --rule:#bdbdbd;
  --paper:#ffffff;
  --band:#ededed;
  --panel:#f5f5f5;
  --btn:#cfcfcf;
}
*{box-sizing:border-box;margin:0;padding:0}
html,body{width:705px;height:1200px;overflow:hidden;background:var(--paper)}
body{position:relative;font-family:"Open Sans",sans-serif;color:var(--ink)}
h1,h2{font-weight:400}
a{text-decoration:none;color:inherit}
.abs{position:absolute}

/* header */
.site-header{left:0;top:0;width:705px;height:73px;background:var(--paper)}
.brand{left:46px;top:14px;display:flex;align-items:center;gap:8px}
.brand-mark{width:46px;height:46px;border-radius:50%;background:var(--brand)}
.brand-name{font-family:"Marcellus",serif;font-size:20px;color:var(--brand)}
.nav-item{top:0;height:73px;display:flex;flex-direction:column;align-items:center;justify-content:center;gap:8px;font-family:"Roboto",sans-serif;font-size:9px;color:var(--ink);text-transform:uppercase;transform:translateX(-50%);white-space:nowrap}
.nav-item svg{width:14px;height:14px;fill:currentColor}
.nav-item.is-active{background:var(--brand);color:#fff;width:61px;transform:none;left:341px;border-bottom:3px solid #4e5fc0}

/* hero */
.hero{left:0;top:73px;width:705px;height:368px;overflow:hidden}
.hero-photo{position:absolute;inset:0;background:linear-gradient(100deg,#5b5a66 0%,#6d6774 18%,#8f7e70 32%,#b9a898 50%,#d3c7bc 72%,#c9beb4 100%)}
.hero-veil{position:absolute;inset:0}
.hero-title{position:absolute;left:225px;top:126px;width:440px;text-align:center;font-family:"Marcellus",serif;font-size:21.5px;line-height:23.5px;color:#fff}
.hero-rule{position:absolute;left:235px;top:213px;width:420px;height:1px;background:rgba(255,255,255,.8)}
.hero-dots{position:absolute;left:429px;top:228px;display:flex;gap:3px}
.hero-dots span{width:9px;height:3px;border:1px solid #fff}
.hero-dots span.on{background:#fff}

/* who we are */
.intro{left:0;top:441px;width:705px;height:208px;background:var(--band);overflow:hidden}
.section-title{font-family:"Roboto Slab",serif;font-size:13px;letter-spacing:2px;color:var(--ink);text-transform:uppercase}
.intro .section-title{position:absolute;left:0;width:705px;top:36px;text-align:center}
.intro .title-rule{position:absolute;top:44px;height:1px;width:120px;background:var(--rule)}
.intro-text{position:absolute;left:102px;width:501px;top:67px;text-align:center;font-size:9.6px;line-height:17px;color:var(--muted)}
.btn-outline{position:absolute;left:296px;top:137px;width:113px;height:37px;border:1px solid #c4c4c4;background:#fafafa;font-family:"Roboto Slab",serif;font-size:11.5px;display:flex;align-items:center;justify-content:center;color:var(--ink)}

/* services */
.services{left:0;top:649px;width:705px;height:214px;background:var(--panel)}
.services-photo{position:absolute;left:0;top:0;width:398px;height:214px;background:linear-gradient(120deg,#cbbfb0 0%,#8e7d6c 35%,#2c3450 60%,#a48a72 100%)}
.services-desk{position:absolute;left:0;top:202px;width:398px;height:12px;background:#8a4f3a}
.services-corner{position:absolute;left:325px;top:0}
.services-body{position:absolute;left:398px;top:0;width:307px;height:214px;text-align:center}
.services-body .section-title{position:absolute;left:0;right:0;top:82px;font-size:13px}
.services-text{position:absolute;left:10px;right:10px;top:115px;font-size:8.4px;line-height:14.6px;color:var(--ink)}
.link-more{position:absolute;left:0;right:0;top:167px;font-family:"Roboto Slab",serif;font-size:10px;text-decoration:underline;color:var(--ink)}

/* connect */
.connect{left:0;top:863px;width:307px;height:214px;background:var(--paper)}
.connect .section-title{position:absolute;left:0;width:307px;top:30px;text-align:center;font-size:13px}
.field{position:absolute;left:45px;width:214px;border:1px solid #c9c9c9;background:#fff;font-family:"Roboto Slab",serif;font-size:7.5px;color:var(--ink);padding:4px 6px}
.btn-submit{position:absolute;left:100px;top:150px;width:92px;height:30px;background:var(--btn);font-family:"Roboto Slab",serif;font-size:10px;display:flex;align-items:center;justify-content:center}
.contact{left:307px;top:863px;width:398px;height:214px;overflow:hidden}
.contact-photo{position:absolute;inset:0;background:linear-gradient(90deg,#3c3f55 0%,#5a5a64 30%,#3a3a3e 50%,#8c8c8c 75%,#b0b0b0 100%)}
.contact-card{position:absolute;left:0;top:0}
.contact-list{position:absolute;left:45px;top:62px;font-size:7.5px;line-height:10px;color:var(--ink)}
.contact-list li{list-style:none;display:flex;gap:6px;margin-bottom:9px;align-items:flex-start}
.contact-list svg{width:11px;height:11px;fill:var(--brand);flex:none}

/* footer */
.site-footer{left:0;top:1077px;width:705px;height:123px;background:var(--band)}
.social{position:absolute;top:31px;width:37px;height:37px;border-radius:50%;border:1px solid #cfcfcf;background:#fff;display:flex;align-items:center;justify-content:center;color:#333}
.social svg{width:12px;height:12px;fill:currentColor}
.social.is-primary{border-color:var(--brand);color:var(--brand)}
.copyright{position:absolute;left:0;width:705px;top:82px;text-align:center;font-size:7.5px;color:#666}
.copyright .name{color:var(--brand);text-transform:uppercase}
</style>
</head>
<body>

<header class="site-header abs">
  <div class="brand abs"><span class="brand-mark"></span><span class="brand-name">CedarBight.Lawyer</span></div>
  <nav>
    <a class="nav-item is-active abs"><svg viewBox="0 0 16 16"><path d="M8 2 1 8h2v6h4v-4h2v4h4V8h2z"/></svg>Home</a>
    <a class="nav-item abs" style="left:433px"><svg viewBox="0 0 16 16"><circle cx="5" cy="5" r="2.5"/><circle cx="11" cy="5" r="2.5"/><path d="M0 13c0-3 2-5 5-5s5 2 5 5zM7 13c0-3 2-5 4-5s5 2 5 5z"/></svg>About us</a>
    <a class="nav-item abs" style="left:499px"><svg viewBox="0 0 16 16"><circle cx="6" cy="9" r="4" fill="none" stroke="currentColor" stroke-width="2.5"/><circle cx="12" cy="4" r="2.5" fill="none" stroke="currentColor" stroke-width="1.8"/></svg>Services</a>
    <a class="nav-item abs" style="left:563px"><svg viewBox="0 0 16 16"><circle cx="8" cy="4.5" r="3.5"/><path d="M1 16c0-5 3-7 7-7s7 2 7 7z"/></svg>Carrers</a>
    <a class="nav-item abs" style="left:632px"><svg viewBox="0 0 16 16"><path d="M3 1l3 3-1.5 2c1 2 3 4 5 5L11.5 9.5l3 3L13 15C7 14 2 9 1 3z"/></svg>Contact us</a>
  </nav>
</header>

<section class="hero abs">
  <div class="hero-photo" role="img" aria-label="Photo of the attorney seated on a stool in a blue suit, in front of a soft-focus hand writing with a pen"></div>
  <svg class="hero-veil" width="705" height="368" viewBox="0 0 705 368">
    <polygon points="680,0 705,0 705,368 330,368" fill="#ffffff" fill-opacity=".28"/>
    <polygon points="690,0 705,0 705,368 345,368" fill="#ffffff" fill-opacity=".12"/>
  </svg>
  <h1 class="hero-title">We are a reputable legal service provider combining legal expertise with an innovative approach to public services</h1>
  <div class="hero-rule"></div>
  <div class="hero-dots"><span></span><span class="on"></span><span></span></div>
</section>

<section class="intro abs">
  <svg class="abs" style="left:0;top:0" width="705" height="208" viewBox="0 0 705 208">
    <polygon points="0,208 210,0 705,0 705,0 495,208" fill="#f5f5f5"/>
    <polygon points="480,208 705,0 705,208" fill="#f2f2f2"/>
  </svg>
  <div class="title-rule" style="left:173px"></div>
  <h2 class="section-title">Who we are</h2>
  <div class="title-rule" style="left:412px"></div>
  <p class="intro-text">We are a reputable legal service provider combining legal expertise with an innovative approach to public services. We strive to provide our clients with low-cost and task-specific legal services through easy access to experienced and competent attorneys in a comfortable environment.</p>
  <a class="btn-outline">READ MORE</a>
</section>

<section class="services abs">
  <div class="services-photo" role="img" aria-label="Photo of a lawyer at his desk on the phone holding a tablet"></div>
  <div class="services-desk"></div>
  <svg class="services-corner" width="146" height="73" viewBox="0 0 146 73">
    <polygon points="0,0 73,0 73,73" fill="var(--brand)"/>
    <polygon points="73,0 146,0 73,73" fill="#c9c9c9"/>
    <g fill="none" stroke="#fff" stroke-width="1.2"><path d="M52 17h8v11h-8M57 22.5h-9M51 19.5l-3 3 3 3"/></g>
    <g fill="none" stroke="#333" stroke-width="1.2"><path d="M88 17h12v11H88M86 22.5h9M92 19.5l3 3-3 3"/></g>
  </svg>
  <div class="services-body">
    <svg class="abs" style="left:109px;top:28px" width="44" height="44" viewBox="0 0 44 44">
      <circle cx="22" cy="22" r="20" fill="none" stroke="#c4c4c4" stroke-width="2"/>
      <g stroke="#b5b5b5" stroke-width="2" fill="none"><path d="M22 10v24M12 15h20M16 34h12"/><path d="M12 15l-5 10h10zM32 15l-5 10h10z"/></g>
    </svg>
    <h2 class="section-title">Lawyer services</h2>
    <p class="services-text">We have many years of experience in all areas of commercial and civil litigation, including tax and licensing disputes. If you are in need of legal representation, our service is always personal.</p>
    <a class="link-more">READ MORE</a>
  </div>
</section>

<section class="connect abs">
  <h2 class="section-title">Connect with us</h2>
  <div class="field" style="top:60px;height:18px">Name</div>
  <div class="field" style="top:80px;height:18px">Email Id</div>
  <div class="field" style="top:100px;height:48px">Message</div>
  <a class="btn-submit">SUBMIT</a>
</section>

<section class="contact abs">
  <div class="contact-photo" role="img" aria-label="Photo of a woman in a dark jacket reading a book outdoors"></div>
  <svg class="contact-card" width="398" height="214" viewBox="0 0 398 214">
    <polygon points="91,1 185,91 91,181 -3,91" fill="#f5f5f5"/>
  </svg>
  <ul class="contact-list">
    <li><svg viewBox="0 0 16 16"><path d="M3 1l3 3-1.5 2c1 2 3 4 5 5L11.5 9.5l3 3L13 15C7 14 2 9 1 3z"/></svg>253-555-0147</li>
    <li><svg viewBox="0 0 16 16"><path d="M1 3h14v2L8 9 1 5zM1 7l7 4 7-4v6H1z"/></svg>morris@cedarbight.lawyer</li>
    <li><svg viewBox="0 0 16 16"><path d="M8 0a5 5 0 0 1 5 5c0 4-5 11-5 11S3 9 3 5a5 5 0 0 1 5-5zm0 3a2 2 0 1 0 0 4 2 2 0 0 0 0-4z"/></svg><span>4120 Harrow Pt. Rd.<br>N., Ellisford, United<br>States</span></li>
  </ul>
</section>

<footer class="site-footer abs">
  <a class="social is-primary" style="left:291px" aria-label="Share"><svg viewBox="0 0 16 16"><circle cx="12" cy="3" r="2.5"/><circle cx="4" cy="8" r="2.5"/><circle cx="12" cy="13" r="2.5"/><path d="M4 8 12 3M4 8l8 5" stroke="currentColor" stroke-width="1.4"/></svg></a>
  <a class="social" style="left:334px" aria-label="Message"><svg viewBox="0 0 16 16"><path d="M1 2h14v9H6l-4 3v-3H1z"/></svg></a>
  <a class="social" style="left:377px" aria-label="Profile"><svg viewBox="0 0 16 16"><circle cx="8" cy="4.5" r="3.5"/><path d="M1 16c0-5 3-7 7-7s7 2 7 7z"/></svg></a>
  <p class="copyright">© <span class="name">CedarBight.Lawyer</span> - 2015. All Rights Reserved.</p>
</footer>

</body>
</html>
```